its a new company based in Christchurch new Zealand building computers ,repairs, upgrades and anything computers for the general public,i like bright happy colours like yellows, greens reds anything that stands out and it needs to communicant trust and security towards my new company,i have no logo yet,

Target Market(s)

target market of all ages

Industry/Entity Type

Building

Contact Information for Business Card

Pixel Harbour Limited,ph-0214862735,email-bluefoxtrail17@mailnest.example,4c marlowe rd,fernvale

```html
<!DOCTYPE html>
<html lang="en">
<head>
<meta charset="utf-8">
<title>Pixel Harbour Limited – Business Card</title>
<link rel="stylesheet" href="https://fonts.googleapis.com/css2?family=Quicksand:wght@500&family=Questrial&display=swap">
<style>
  :root {
    --card-black: #050505;
    --brand-pink: #f0145e;
    --lime: #a6f01e;
    --green-soft-start: #7fd811;
    --green-soft-end: #b2f229;
    --navy: #14283a;
  }
  html, body {
    margin: 0;
    padding: 0;
    overflow: hidden;
    background: #ffffff;
  }
  .card {
    position: relative;
    width: 1200px;
    height: 741px;
    overflow: hidden;
    background: var(--card-black);
  }
  .wave-band {
    position: absolute;
    inset: 0;
    width: 1200px;
    height: 741px;
  }
  .brand-mark {
    position: absolute;
    left: 54px;
    top: 120px;
    width: 210px;
    text-align: center;
  }
  .brand-mark__square {
    width: 130px;
    height: 130px;
    margin: 0 auto 16px;
    background: var(--navy);
  }
  .brand-mark__name {
    font-family: "Quicksand", sans-serif;
    font-weight: 500;
    color: var(--brand-pink);
    font-size: 28px;
    line-height: 1;
    white-space: nowrap;
  }
  .company-name {
    position: absolute;
    left: 274px;
    top: 68px;
    margin: 0;
    font-family: "Quicksand", sans-serif;
    font-weight: 500;
    font-size: 72px;
    line-height: 1.1;
    color: var(--brand-pink);
    white-space: nowrap;
  }
  .contact {
    position: absolute;
    left: 300px;
    top: 215px;
    margin: 0;
    padding: 0;
    list-style: none;
  }
  .contact__item {
    display: flex;
    align-items: center;
    height: 100px;
    font-family: "Questrial", sans-serif;
    font-size: 44px;
    color: var(--lime);
    white-space: nowrap;
  }
  .contact__icon {
    width: 62px;
    height: 48px;
    margin-right: 29px;
    flex: none;
  }
</style>
</head>
<body>
  <div class="card">
    <svg class="wave-band" viewBox="0 0 1200 741" role="img" aria-label="Bright green decorative wave across the bottom of the card">
      <defs>
        <linearGradient id="wave-fill" x1="0" y1="0" x2="1" y2="0">
          <stop offset="0" stop-color="var(--green-soft-start)"/>
          <stop offset="1" stop-color="var(--green-soft-end)"/>
        </linearGradient>
      </defs>
      <path d="M0,395 C200,540 440,605 650,600 C860,592 1050,540 1200,490 L1200,741 L0,741 Z" fill="url(#wave-fill)"/>
    </svg>

    <div class="brand-mark">
      <div class="brand-mark__square"></div>
      <div class="brand-mark__name">Pixel Harbour</div>
    </div>

    <h1 class="company-name">Pixel Harbour Limited</h1>

    <ul class="contact">
      <li class="contact__item">
        <svg class="contact__icon" viewBox="0 0 62 48" aria-hidden="true">
          <path d="M4,16 C4,6 58,6 58,16 L58,20 L44,20 L44,14 C38,11 24,11 18,14 L18,20 L4,20 Z" fill="var(--lime)"/>
          <path d="M14,22 L48,22 L56,46 L6,46 Z" fill="var(--lime)"/>
          <circle cx="31" cy="34" r="7" fill="var(--card-black)"/>
          <circle cx="31" cy="34" r="3" fill="var(--lime)"/>
        </svg>
        <span>0214862735</span>
      </li>
      <li class="contact__item">
        <svg class="contact__icon" viewBox="0 0 62 48" aria-hidden="true">
          <rect x="3" y="6" width="56" height="36" fill="var(--lime)"/>
          <path d="M3,6 L31,28 L59,6" fill="none" stroke="var(--card-black)" stroke-width="3"/>
          <path d="M3,42 L24,23 M59,42 L38,23" fill="none" stroke="var(--card-black)" stroke-width="3"/>
        </svg>
        <span>bluefoxtrail17@mailnest.example,</span>
      </li>
      <li class="contact__item">
        <svg class="contact__icon" viewBox="0 0 62 48" aria-hidden="true">
          <path d="M31,48 C23,34 15,26 15,16 A16,16 0 0 1 47,16 C47,26 39,34 31,48 Z" fill="var(--lime)"/>
          <circle cx="31" cy="16" r="6" fill="var(--card-black)"/>
        </svg>
        <span>4c Marlowe Rd,Fernvale</span>
      </li>
    </ul>
  </div>
</body>
</html>
```